****Business Card Design for Cormorant Ridge. Design based around attached logo/company name

I’m looking for business card design for my company Cormorant Ridge Holdings,LLC. Design should be professional, sharp and minimal. Outside of the attached logos, greyscale colors for remainder of cards. My thoughts are two-sided card with attached logo on one side and my info on the other but open to one-sided as well with right design.
Target Market(s)
Real estate professionals including banks, private investors, property owners, developers, commercial tenants like Brewloft, Grocana or Tandberry’s.
Industry/Entity Type
Commercial real estate development and investments.
Contact Information for Business Card
Name, title, email, phone #’s, web address and physical address
Font styles to use
Other font styles liked:
- Helvetica, Garamond, etc
Colors
Designer to choose only greyscale colors for use in the design.
Requirements
Must have
- Attached logo first or second options.
Nice to have
- Two sided card with logo on one side. Attached Logo/company name can be laid out any way that flows as long as it’s legible.name
Should not have
- No loud colors. ***Please do not include logo, I have removed the company design with a logo image.

```html
<!DOCTYPE html>
<html lang="en">
<head>
<meta charset="utf-8">
<title>Cormorant Ridge Holdings – Business Card</title>
<link href="https://fonts.googleapis.com/css2?family=Cormorant+Garamond:wght@500&family=Roboto:wght@400&display=swap" rel="stylesheet">
<style>
  :root {
    --backdrop: #999a99;
    --card-white: #fcfcfc;
    --slate: #5d6474;
    --ink: #5a5f6b;
    --text-light: #ffffff;
  }
  * { margin: 0; padding: 0; box-sizing: border-box; }
  html, body {
    width: 1200px; height: 1200px; overflow: hidden;
    background: var(--backdrop);
  }
  .card {
    position: absolute;
    left: 231px;
    width: 736px;
    height: 451px;
  }
  .card--front { top: 116px; background: var(--card-white); }
  .card--back { top: 631px; background: var(--slate); }

  .brand-box {
    position: absolute;
    left: 45px; top: 178px;
    width: 300px; height: 97px;
    background: var(--slate);
    display: flex; align-items: center; justify-content: center;
  }
  .brand-name {
    font-family: "Cormorant Garamond", serif;
    font-weight: 500;
    color: var(--text-light);
    text-transform: uppercase;
    text-align: center;
    letter-spacing: 0.04em;
  }
  .brand-box .brand-name { font-size: 22px; line-height: 1.15; }

  .divider {
    position: absolute;
    left: 381px; top: 120px;
    width: 2px; height: 212px;
    background: var(--slate);
  }
  .person {
    position: absolute;
    left: 412px; top: 112px;
    font-family: "Roboto", sans-serif;
    color: var(--ink);
  }
  .person__name { font-size: 30px; line-height: 36px; text-transform: uppercase; }
  .person__title { font-size: 23px; line-height: 30px; }

  .contact-list {
    position: absolute;
    left: 412px; top: 208px;
    list-style: none;
    font-family: "Roboto", sans-serif;
    font-size: 21px;
    color: var(--ink);
  }
  .contact-list li {
    display: flex; align-items: center;
    height: 33px;
  }
  .contact-list svg {
    width: 22px; height: 22px;
    margin-right: 10px;
    fill: none; stroke: var(--slate); stroke-width: 1.8;
  }

  .card--back .brand-name {
    position: absolute;
    left: 0; right: 0; top: 155px;
    font-size: 56px;
    line-height: 1.1;
  }
</style>
</head>
<body>
  <section class="card card--front">
    <div class="brand-box">
      <p class="brand-name">Cormorant Ridge<br>Holdings, LLC</p>
    </div>
    <div class="divider"></div>
    <div class="person">
      <p class="person__name">Marlon Keats</p>
      <p class="person__title">President</p>
    </div>
    <ul class="contact-list">
      <li>
        <svg viewBox="0 0 24 24"><rect x="6" y="2" width="12" height="20" rx="2"/><line x1="11" y1="18" x2="13" y2="18"/></svg>
        014 2875 3690
      </li>
      <li>
        <svg viewBox="0 0 24 24"><path d="M3 9c0-3 4-4 9-4s9 1 9 4v1h-4V8H7v2H3z"/><path d="M6 12h12l2 8H4z"/><circle cx="12" cy="16" r="2"/></svg>
        014 2875 3690
      </li>
      <li>
        <svg viewBox="0 0 24 24"><rect x="2" y="5" width="17" height="12"/><polyline points="2,5 10.5,12 19,5"/><circle cx="19" cy="18" r="3.5"/></svg>
        hello@cormorantridge.com
      </li>
      <li>
        <svg viewBox="0 0 24 24"><circle cx="12" cy="12" r="9"/><ellipse cx="12" cy="12" rx="4" ry="9"/><line x1="3" y1="12" x2="21" y2="12"/><line x1="5" y1="7" x2="19" y2="7"/><line x1="5" y1="17" x2="19" y2="17"/></svg>
        www.cormorantridge.com
      </li>
    </ul>
  </section>

  <section class="card card--back">
    <p class="brand-name">Cormorant Ridge<br>Holdings, LLC</p>
  </section>
</body>
</html>
```